Financial Services Consultant needs a business card

We need a business card for a new consulting company based in Melbourne called
"Korvane Metrics". Tagline is Measure, Monitor, Save
We would like to see business card designs that are in line with the minimal style of the website www.korvane-metrics-example.com
The font I have used on the website is Proxima Nova and would like the same or similar font used on the business card with a minimal design in line with the website Two sided with "KORVANE METRICS" MEASURE, MONITOR, SAVE on one side and name, title and contact details on the otther
Updates

Hi All, thanks for your submissions, much appreciated.

I have recently added some colour to my webiste, it is hex #3a7b74 for those that wish to use it
Thanks

Hi all

thanks very much for your design submissions I am very impressed and they are much appreciated.

Interms of general feedback please find below;

Colour: I am trying to stick to a minimal design and colour scheme for my website which is still under construction, up to 3 colours( www.korvane-metrics-example.com) it is currently black and white with a small amount of blue/green but I am open to suggestion/interpretations for a consulting company.

Card: I dont mind if it has rounded edges or straight, I was thinking about using a letterpress card if possible

Detail: the detail on the card will include; Name, Title, Mobile, Personal Email, Business Email,Web,Business Address

Once again thanks for submissions

Industry/Entity Type

Business

```html
<!DOCTYPE html>
<html lang="en">
<head>
<meta charset="utf-8">
<title>Korvane Metrics – Business Card</title>
<link rel="stylesheet" href="https://fonts.googleapis.com/css2?family=Arimo:ital,wght@0,400;0,700;1,400&family=Jost:wght@300;400;500&display=swap">
<style>
  :root {
    --stage: #0e0e0e;
    --card-top: #3a3a3a;
    --card-bottom: #1f1f1f;
    --band-top: #5d5d5d;
    --band-bottom: #434343;
    --pattern-light: #363636;
    --pattern-dark: #262626;
    --text-bright: #e6e6e6;
    --text-soft: #c8c8c8;
    --text-muted: #8a8a8a;
    --text-faint: #6e6e6e;
    --accent: #3aa6d8;
  }
  html, body {
    margin: 0;
    width: 1200px;
    height: 900px;
    overflow: hidden;
    background: var(--stage);
  }
  .stage {
    position: relative;
    width: 1200px;
    height: 900px;
  }
  .card {
    position: absolute;
    left: 370px;
    width: 448px;
    height: 268px;
    overflow: hidden;
    background: linear-gradient(180deg, var(--card-top), var(--card-bottom));
    box-shadow: 0 2px 6px rgba(0,0,0,.7), inset 0 1px 0 rgba(255,255,255,.08);
  }
  .card--contact { top: 133px; }
  .card--brand { top: 452px; }

  /* Contact side */
  .contact__wordmark {
    position: absolute;
    left: 95px;
    top: 46px;
    margin: 0;
    font: 700 13px/1 "Arimo", Arial, sans-serif;
    letter-spacing: .5px;
    color: var(--text-muted);
  }
  .contact__band {
    position: absolute;
    left: 0;
    top: 144px;
    width: 399px;
    height: 61px;
    background: linear-gradient(180deg, var(--band-top), var(--band-bottom));
  }
  .contact__details {
    position: absolute;
    right: 52px;
    top: 146px;
    text-align: right;
    font-family: "Arimo", Arial, sans-serif;
    color: var(--text-soft);
  }
  .contact__name { margin: 0; font-size: 12px; font-weight: 700; line-height: 15px; color: var(--text-bright); }
  .contact__title { margin: 0; font-size: 10px; font-style: italic; line-height: 14px; color: var(--accent); }
  .contact__line { margin: 0; font-size: 10px; line-height: 14px; }
  .contact__web {
    position: absolute;
    left: 0;
    right: 0;
    top: 243px;
    margin: 0;
    text-align: center;
    font: 400 10px/1 "Arimo", Arial, sans-serif;
    letter-spacing: 2.6px;
    color: var(--text-faint);
  }

  /* Brand side */
  .brand__pattern {
    position: absolute;
    inset: 0;
    background: repeating-linear-gradient(180deg, var(--pattern-light) 0 9px, var(--pattern-dark) 9px 16px);
    opacity: .45;
  }
  .brand__tagline {
    position: absolute;
    margin: 0;
    font: 400 13px/1 "Jost", "Futura", sans-serif;
    letter-spacing: .6px;
    color: var(--text-bright);
  }
  .brand__tagline--measure { left: 261px; top: 40px; }
  .brand__tagline--monitor { left: 228px; top: 72px; }
  .brand__tagline--save { left: 360px; top: 104px; }
  .brand__wordmark {
    position: absolute;
    left: 63px;
    top: 194px;
    margin: 0;
    font: 500 21px/1 "Jost", "Futura", sans-serif;
    letter-spacing: 2px;
    color: var(--text-soft);
  }
</style>
</head>
<body>
<main class="stage">
  <section class="card card--contact" aria-label="Contact side">
    <p class="contact__wordmark">KORVANE METRICS</p>
    <div class="contact__band"></div>
    <div class="contact__details">
      <p class="contact__name">Daniel Mercer</p>
      <p class="contact__title">CEO</p>
      <p class="contact__line">(555) 014-2290</p>
      <p class="contact__line">d.mercer@korvane-metrics-example.com</p>
    </div>
    <p class="contact__web">www.korvane-metrics-example.com</p>
  </section>

  <section class="card card--brand" aria-label="Brand side">
    <div class="brand__pattern" role="img" aria-label="Faint repeating background pattern of the tagline words"></div>
    <p class="brand__tagline brand__tagline--measure">MEASURE</p>
    <p class="brand__tagline brand__tagline--monitor">MONITOR</p>
    <p class="brand__tagline brand__tagline--save">SAVE</p>
    <p class="brand__wordmark">KORVANE METRICS</p>
  </section>
</main>
</body>
</html>
```